Cardiology Practice needs a Heart Scan Order Form

Busy cardiology practice needs an order form for a heart scan test. Sample is attached. One side should have all information noted and the other side should have our physician names (Vikram Joshi, MD, K.L. Morvandi, MD, Anjali Desai, MD, Parvin Joshi, MD, and Gerald Montefino, MD. It should have the map that is uploaded and our demographic information (Crestline Cardio PLLC, 218 Juniper Ave. Ste. B, Lakemont, NM 77412 along with phone 713-642-1187 and fax 713-642-1188) as well as our web address (crestlinecardio.example). Our primary colors are red, black and white. Needs to fit paper size 8 1/2 by 11.

Target Market(s)

Healthcare

Industry/Entity Type

Health Care

Font styles to use
Serif

Colors
ec1f27

Requirements
Must have
• Logo, information listed on sample form, demographics and physician names as well as website.
Nice to have
• Open to suggestions
Should not have
• Physician Pictures

```html
<!DOCTYPE html>
<html lang="en">
<head>
<meta charset="utf-8">
<title>Calcium Score Heart Scan – Order Form</title>
<link rel="stylesheet" href="https://fonts.googleapis.com/css2?family=Open+Sans:wght@300;400;600;700;800&display=swap">
<style>
  :root {
    --brand-red: #c1343c;
    --ink: #1f1f1f;
    --rule: #2a2a2a;
    --paper: #ffffff;
    --backdrop: #e8e6e6;
    --dots: #555555;
  }
  * { box-sizing: border-box; margin: 0; padding: 0; }
  html, body {
    width: 907px; height: 1200px; overflow: hidden;
    background: var(--backdrop);
    font-family: "Open Sans", Arial, sans-serif;
    color: var(--ink);
  }
  .order-form {
    position: absolute; left: 66px; top: 95px;
    width: 774px; height: 1000px;
    background: var(--paper);
  }
  .form-header {
    position: absolute; left: 0; top: 0; width: 100%; height: 118px;
    background: var(--brand-red);
    border-bottom: 3px solid var(--rule);
  }
  .brand {
    position: absolute; left: 32px; top: 40px;
    display: flex; align-items: center; gap: 8px;
    color: #fff; font-weight: 700; font-size: 17px; letter-spacing: 0.5px;
  }
  .brand-mark { width: 14px; height: 14px; border: 2px solid #fff; border-radius: 50%; }
  .form-title {
    position: absolute; left: 200px; width: 380px; top: 22px;
    text-align: center; color: #fff; font-weight: 800;
    font-size: 33px; line-height: 41px; letter-spacing: 0.3px;
  }
  .test-schedule {
    position: absolute; left: 601px; top: 30px; width: 146px; height: 68px;
    background: #fff; border: 1.5px solid var(--rule);
    font-size: 10px;
  }
  .test-schedule h2 {
    font-size: 11.5px; font-weight: 600; text-align: center;
    height: 22px; line-height: 22px; border-bottom: 1.5px solid var(--rule);
  }
  .test-schedule p { height: 22px; line-height: 22px; padding-left: 5px; }
  .test-schedule p + p { border-top: 1.5px solid var(--rule); }

  .form-section {
    position: absolute; left: 0; width: 100%;
    border-bottom: 2px solid var(--rule);
  }
  .section-number {
    position: absolute; left: 22px; top: 12px;
    font-size: 44px; font-weight: 300; line-height: 1;
  }
  .section-label {
    position: absolute; left: 56px; top: 16px;
    writing-mode: vertical-rl; transform: rotate(180deg);
    color: var(--brand-red); font-weight: 700; font-size: 10.5px;
    line-height: 12px; text-align: center; letter-spacing: 0.4px;
  }
  .field-list { position: absolute; left: 100px; width: 645px; top: 15px; }
  .field {
    display: flex; align-items: baseline; height: 23px; font-size: 11px;
  }
  .field-label { width: 140px; text-align: right; padding-right: 4px; }
  .field-line { flex: 1; border-bottom: 1.5px dotted var(--dots); height: 9px; }

  .medical-row {
    position: absolute; display: flex; align-items: center; font-size: 11px; white-space: nowrap;
  }
  .box {
    display: inline-block; width: 11px; height: 11px;
    border: 1px solid #444; margin-right: 7px; vertical-align: -1px;
  }
  .sex-box {
    display: inline-block; width: 15px; height: 15px; border: 1px solid #444;
    font-size: 9.5px; line-height: 13px; text-align: center; margin-left: 5px;
  }
  .inline-field { display: inline-flex; align-items: baseline; }
  .inline-field .blank { display: inline-block; border-bottom: 1.5px dotted var(--dots); margin-left: 4px; }
  .check-row { position: absolute; left: 182px; font-size: 11px; white-space: nowrap; }
  .check-row span { position: absolute; white-space: nowrap; }

  .instruction-lead {
    position: absolute; left: 91px; top: 20px;
    font-size: 10.5px; font-weight: 700;
  }
  .instruction-list { position: absolute; left: 210px; top: 42px; width: 540px; list-style: none; }
  .instruction-list li {
    position: relative; padding-left: 20px; font-size: 10.5px; line-height: 13px;
    margin-bottom: 5px;
  }
  .instruction-list li::before {
    content: ""; position: absolute; left: 0; top: 2px;
    width: 9px; height: 9px; border: 1px solid #444;
  }
  .certification-text {
    position: absolute; left: 91px; top: 18px; width: 640px;
    font-size: 10.5px; font-weight: 700; line-height: 13px;
  }
  .sign-row { position: absolute; left: 91px; font-size: 10.5px; }
  .sign-row .inline-field { position: absolute; white-space: nowrap; }
  .practice-info {
    position: absolute; left: 91px; top: 134px; font-size: 10.5px; line-height: 13px;
  }
  .referring-box {
    position: absolute; left: 590px; top: 72px; width: 159px; height: 96px;
    border: 1.5px solid var(--rule); font-size: 10px;
  }
  .referring-box h3 {
    font-size: 9px; font-weight: 400; text-align: center; line-height: 11px;
    padding: 3px 4px; border-bottom: 1.5px solid var(--rule); height: 30px;
  }
  .referring-box p { height: 22px; line-height: 22px; padding-left: 6px; }
  .referring-box p + p { border-top: 1.5px solid var(--rule); }
  .form-footer {
    position: absolute; left: 0; bottom: 0; width: 100%; height: 32px;
    background: var(--brand-red); border-top: 3px solid var(--rule);
  }
</style>
</head>
<body>
<main class="order-form">
  <header class="form-header">
    <div class="brand"><span class="brand-mark"></span>CRESTLINE CARDIO</div>
    <h1 class="form-title">CALCIUM SCORE<br>HEART SCAN</h1>
    <div class="test-schedule">
      <h2>TEST SCHEDULE</h2>
      <p>Test date:</p>
      <p>Test time:</p>
    </div>
  </header>

  <section class="form-section" style="top:121px;height:142px;">
    <div class="section-number">1</div>
    <div class="section-label">PATIENT<br>INFORMATION</div>
    <div class="field-list" style="top:16px;">
      <div class="field"><span class="field-label">Last name:</span><span class="field-line"></span></div>
      <div class="field"><span class="field-label">First name:</span><span class="field-line"></span></div>
      <div class="field"><span class="field-label">MI:</span><span class="field-line"></span></div>
      <div class="field"><span class="field-label">Date of birth:</span><span class="field-line"></span></div>
      <div class="field"><span class="field-label">Account no.:</span><span class="field-line"></span></div>
    </div>
  </section>

  <section class="form-section" style="top:263px;height:133px;">
    <div class="section-number">2</div>
    <div class="section-label">CONTACT<br>INFORMATION</div>
    <div class="field-list" style="top:16px;">
      <div class="field"><span class="field-label">Address:</span><span class="field-line"></span></div>
      <div class="field"><span class="field-label">Home phone no.:</span><span class="field-line"></span></div>
      <div class="field"><span class="field-label">Mobile phone no.:</span><span class="field-line"></span></div>
    </div>
  </section>

  <section class="form-section" style="top:396px;height:155px;">
    <div class="section-number">3</div>
    <div class="section-label">MEDICAL<br>INFORMATION</div>
    <div class="medical-row" style="left:216px;top:20px;">
      Sex:<span class="sex-box">F</span><span class="sex-box">M</span>
    </div>
    <div class="medical-row" style="left:321px;top:22px;">
      <span class="inline-field">Hight:<span class="blank" style="width:82px;"></span></span>
    </div>
    <div class="medical-row" style="left:464px;top:22px;">
      <span class="inline-field">Weight:<span class="blank" style="width:88px;"></span></span>
    </div>
    <div class="medical-row" style="left:625px;top:22px;">
      <span class="inline-field">Race:<span class="blank" style="width:80px;"></span></span>
    </div>
    <div class="medical-row" style="left:182px;top:44px;width:557px;">
      <span class="inline-field" style="width:100%;">Diagnosis:<span class="blank" style="flex:1;"></span></span>
    </div>
    <div class="check-row" style="top:72px;">
      <span style="left:0;"><i class="box"></i>PCI (no. of stents: ............. )</span>
      <span style="left:192px;"><i class="box"></i>CABG (no. of vessels: ................ )</span>
      <span style="left:402px;"><i class="box"></i>MI (last event: ................)</span>
    </div>
    <div class="check-row" style="top:95px;">
      <span style="left:0;"><i class="box"></i>PCM/ICD</span>
      <span style="left:94px;"><i class="box"></i>Diabetes</span>
      <span style="left:185px;"><i class="box"></i>Claustrophobia</span>
      <span style="left:317px;"><i class="box"></i>Asthma</span>
      <span style="left:402px;"><i class="box"></i>Emphysema</span>
      <span style="left:507px;"><i class="box"></i>COPD</span>
    </div>
    <div class="check-row" style="top:118px;">
      <span style="left:0;"><i class="box"></i>LMP: ...............</span>
      <span style="left:120px;"><i class="box"></i>bHCG</span>
      <span style="left:185px;"><i class="box"></i>Tubal ligation</span>
      <span style="left:297px;"><i class="box"></i>Post-menopause &gt; 1 year</span>
      <span style="left:466px;"><i class="box"></i>Hysterectomy</span>
    </div>
  </section>

  <section class="form-section" style="top:551px;height:222px;">
    <div class="section-number">4</div>
    <div class="section-label">INSTRUCTION</div>
    <p class="instruction-lead">Please read the following instructions carefully. You might be rescheduled if any of the following instructions are not met.</p>
    <ul class="instruction-list">
      <li>AVOID caffeine containing products (coffee, tea, soda, chocolate, energy drinks, or some over the<br>counter medications) for 4 hours prior to testing.</li>
      <li>AVOID smoking for 4 hours prior to testing.</li>
      <li>AVOID eating or drinking anything except water for 4 hours prior to testing.</li>
      <li>Arrive 15 minutes early for your appointment time.</li>
      <li>Wear comfortable clothing. Remove any metal objects, such as jewelry or piercings.<br>Women will be asked to remove bras containing metal underwire.</li>
      <li>Inform your physician or the staff if you are claustrophobic or have a problem staying in restricted<br>environments for any length of time.</li>
      <li>Inform the physician or the staff if you are or think you might be pregnant.</li>
    </ul>
  </section>

  <section class="form-section" style="top:773px;height:195px;border-bottom:none;">
    <div class="section-number">5</div>
    <div class="section-label">CERTIFICATION</div>
    <p class="certification-text">I hereby acknowledge that the instructions and procedures pertinent to this study were explained thoroughly,<br>I had time to ask questions, and these questions were addressed satisfactorily.</p>
    <div class="sign-row" style="top:66px;">
      <span class="inline-field" style="left:0;">Patient's print name:<span class="blank" style="width:128px;"></span></span>
      <span class="inline-field" style="left:249px;">Patient's signature:<span class="blank" style="width:122px;"></span></span>
    </div>
    <div class="sign-row" style="top:92px;">
      <span class="inline-field" style="left:0;">Prescriber's print name:<span class="blank" style="width:108px;"></span></span>
      <span class="inline-field" style="left:244px;">Prescriber's signature:<span class="blank" style="width:112px;"></span></span>
    </div>
    <p class="practice-info">Crestline Cardio, PLLC. Visit us at 218 Juniper Ave. Ste. B, Lakemont, NM 77412.<br>For appointments or more information on testing,<br>please call (713) 642 1187, or visit www.crestlinecardio.example.</p>
    <div class="referring-box">
      <h3>REFERRING PHYSICIAN CONTACT INFORMATION</h3>
      <p>Order Date:</p>
      <p>Tel no.:</p>
      <p>Fax no.:</p>
    </div>
  </section>

  <footer class="form-footer"></footer>
</main>
</body>
</html>
```